New Business Card Design*

We are a recruitment company based in Norwich/Cambridge England.
I have included our company logo which we want to remain the same.

What we are looking for is a new creative Business card which will really stand out!!

Contact Information for Business Card

Harriet Vance
email: Harriet@brelvix.co.uk
Address: Tolworth House
Ashgrove Innovation Park
Pelham Road
Norwich
KT9 3QD
Tel:01632 960418

```html
<!DOCTYPE html>
<html lang="en">
<head>
<meta charset="utf-8">
<title>Brelvix Business Card</title>
<link rel="stylesheet" href="https://fonts.googleapis.com/css2?family=Montserrat:wght@500;600&family=Oswald:wght@500&family=Work+Sans:wght@400;500&display=swap">
<style>
  :root {
    --backdrop: #161616;
    --card: #262626;
    --card-edge: #2f2f2f;
    --green: #7cc242;
    --white: #f2f2f2;
  }
  html, body {
    margin: 0;
    width: 1200px;
    height: 900px;
    overflow: hidden;
    background: var(--backdrop);
  }
  .canvas {
    position: relative;
    width: 1200px;
    height: 900px;
  }
  .card {
    position: absolute;
    left: 280px;
    width: 640px;
    height: 360px;
    background: linear-gradient(135deg, var(--card) 0%, var(--card-edge) 100%);
    border-bottom: 5px solid var(--green);
    box-sizing: border-box;
    box-shadow: 0 10px 30px rgba(0,0,0,0.5);
  }
  .card--front { top: 50px; }
  .card--back { top: 475px; }

  /* Front */
  .brand {
    position: absolute;
    top: 108px;
    left: 0;
    right: 0;
    display: flex;
    justify-content: center;
    align-items: center;
    gap: 18px;
  }
  .brand__dot {
    width: 70px;
    height: 70px;
    border-radius: 50%;
    background: var(--green);
  }
  .brand__block { display: flex; flex-direction: column; }
  .brand__name {
    font-family: "Montserrat", sans-serif;
    font-weight: 600;
    font-size: 56px;
    line-height: 1;
    color: var(--white);
    letter-spacing: -1px;
  }
  .brand__tagline {
    margin-top: 6px;
    font-family: "Montserrat", sans-serif;
    font-weight: 600;
    font-size: 10px;
    letter-spacing: 5px;
    color: var(--white);
  }
  .front__url {
    position: absolute;
    bottom: 34px;
    left: 0;
    right: 0;
    text-align: center;
    font-family: "Work Sans", sans-serif;
    font-size: 16px;
    letter-spacing: 1.5px;
    color: var(--white);
  }
  .accent { color: var(--green); }

  /* Back */
  .identity {
    position: absolute;
    top: 140px;
    left: 60px;
    width: 250px;
    text-align: right;
  }
  .identity__name {
    font-family: "Oswald", sans-serif;
    font-weight: 500;
    font-size: 38px;
    line-height: 1;
    color: var(--green);
    text-transform: uppercase;
    letter-spacing: 0.5px;
  }
  .identity__role {
    margin-top: 6px;
    font-family: "Work Sans", sans-serif;
    font-size: 18px;
    letter-spacing: 1px;
    color: var(--white);
  }
  .divider {
    position: absolute;
    top: 132px;
    left: 334px;
    width: 2px;
    height: 76px;
    background: var(--green);
  }
  .contacts {
    position: absolute;
    top: 134px;
    left: 358px;
    margin: 0;
    padding: 0;
    list-style: none;
    font-family: "Work Sans", sans-serif;
    font-size: 17px;
    letter-spacing: 1px;
    color: var(--white);
  }
  .contacts li {
    display: flex;
    align-items: center;
    gap: 12px;
    height: 25px;
  }
  .contacts svg { width: 12px; height: 12px; flex: none; }
  .address {
    position: absolute;
    bottom: 36px;
    left: 60px;
    font-family: "Work Sans", sans-serif;
    font-size: 17px;
    letter-spacing: 1.5px;
    color: var(--white);
  }
</style>
</head>
<body>
<main class="canvas">
  <section class="card card--front">
    <div class="brand">
      <div class="brand__dot"></div>
      <div class="brand__block">
        <span class="brand__name">Brelvix</span>
        <span class="brand__tagline">Technology Recruitment</span>
      </div>
    </div>
    <p class="front__url">www.<span class="accent">brelvix</span>.co.uk</p>
  </section>

  <section class="card card--back">
    <div class="identity">
      <div class="identity__name">Harriet Vance</div>
      <div class="identity__role">Founder</div>
    </div>
    <div class="divider"></div>
    <ul class="contacts">
      <li>
        <svg viewBox="0 0 24 24" aria-hidden="true"><path fill="#7cc242" d="M6.6 10.8a15 15 0 0 0 6.6 6.6l2.2-2.2c.3-.3.7-.4 1-.2 1.1.4 2.3.6 3.6.6.6 0 1 .4 1 1V20c0 .6-.4 1-1 1A17 17 0 0 1 3 4c0-.6.4-1 1-1h3.5c.6 0 1 .4 1 1 0 1.3.2 2.5.6 3.6.1.3 0 .7-.2 1z"/></svg>
        <span>01632 960418</span>
      </li>
      <li>
        <svg viewBox="0 0 24 24" aria-hidden="true"><rect x="2" y="5" width="20" height="14" fill="none" stroke="#7cc242" stroke-width="2"/><path d="M2 5l10 8 10-8" fill="none" stroke="#7cc242" stroke-width="2"/></svg>
        <span>info@brelvix.co.uk</span>
      </li>
      <li>
        <svg viewBox="0 0 24 24" aria-hidden="true"><g fill="none" stroke="#7cc242" stroke-width="2"><circle cx="12" cy="12" r="10"/><ellipse cx="12" cy="12" rx="4" ry="10"/><path d="M2 12h20"/></g></svg>
        <span>www.<span class="accent">brelvix</span>.co.uk</span>
      </li>
    </ul>
    <p class="address">Tolworth House, Pelham Road KT9 3QD Norwich</p>
  </section>
</main>
</body>
</html>
```